KELVA GIFTS - Gift Card app

We have created an application to sell gift cards and greeting cards for Brindle Shop and Mervox Hub. Layout to remain the same, upgrade and change the graphics. Keep the background white. Must fit into existing app.

Logo design + 4 tutorial slides + 1 main page. The 5 current images are included and red box around what we want changed.

Pay particular attention to the red squares.

```html
<!DOCTYPE html>
<html lang="en">
<head>
<meta charset="utf-8">
<title>KELVA GIFTS – App Screens</title>
<link href="https://fonts.googleapis.com/css2?family=Inter:wght@400;500;600&family=Rubik:wght@500;600;700&display=swap" rel="stylesheet">
<style>
  :root{
    --brand-red:#b0231f;
    --brand-red-dark:#9c1c19;
    --brand-red-soft:#c4403a;
    --page-bg:#e3e3e3;
    --white:#ffffff;
    --ink:#222222;
    --ink-muted:#7a7a7a;
    --line:#dedede;
    --dot:#e6e6e6;
  }
  *{box-sizing:border-box;margin:0;padding:0}
  html,body{width:687px;height:1200px;overflow:hidden;background:var(--page-bg)}
  body{position:relative;font-family:"Inter",sans-serif;color:var(--ink)}
  .screen{position:absolute;width:222px;height:472px;border-radius:28px;overflow:hidden;background:var(--white)}
  .screen--splash{left:69px;top:68px;background:var(--brand-red)}
  .screen--login{left:390px;top:68px}
  .screen--recipient{left:69px;top:648px}
  .screen--tutorial{left:390px;top:648px}

  .status{position:absolute;top:0;left:0;right:0;height:26px;display:flex;align-items:center;justify-content:space-between;padding:0 14px 0 16px;color:var(--white);font-size:8.5px;font-weight:600;z-index:3}
  .status svg{display:block}
  .notch{position:absolute;top:0;left:50%;transform:translateX(-50%);width:122px;height:18px;background:#111;border-radius:0 0 12px 12px;z-index:4}

  .wordmark{font-family:"Rubik",sans-serif;font-weight:700;color:var(--white);letter-spacing:.12em;white-space:nowrap}
  .splash-mark{position:absolute;top:170px;left:0;right:0;display:flex;flex-direction:column;align-items:center;gap:12px}
  .splash-mark .box{width:48px;height:48px;background:var(--white);border-radius:4px}
  .splash-mark .wordmark{font-size:17px}
  .art{position:absolute}
  .art--party{left:0;right:0;bottom:0;height:112px;background:linear-gradient(180deg,rgba(176,35,31,0) 0%,#e8702a 45%,#f29a2e 100%)}

  .login-hero{position:absolute;left:0;right:0;top:0;height:180px;background:var(--brand-red)}
  .art--card{left:30px;top:36px;width:170px;height:118px;border-radius:10px;background:linear-gradient(135deg,#f1c232 0%,#f6e7d8 55%,#d9d0c4 100%)}
  .login-sheet{position:absolute;left:0;right:0;top:167px;bottom:0;background:var(--white);border-radius:16px 16px 0 0;padding:0 15px}
  .title{font-family:"Rubik",sans-serif;font-weight:600;text-align:center;color:var(--ink)}
  .login-sheet .title{font-size:15px;margin-top:23px}
  .lead{font-size:8px;line-height:14px;color:var(--ink-muted);text-align:center}
  .login-sheet .lead{margin-top:5px}
  .field-label{font-size:7px;font-weight:500;color:var(--ink);margin-bottom:5px;display:block}
  .field-label .req{color:var(--brand-red);margin-left:3px}
  .field-label .opt{color:var(--ink-muted);font-weight:400}
  .input{height:23px;border:1px solid var(--line);border-radius:3px;position:relative}
  .input svg{position:absolute;right:8px;top:50%;transform:translateY(-50%)}
  .btn{display:flex;align-items:center;justify-content:center;height:23px;background:var(--brand-red);color:var(--white);border-radius:3px;font-size:9px;font-weight:500}
  .login-form{margin-top:18px}
  .login-form .field{margin-bottom:11px}
  .remember-row{display:flex;align-items:center;justify-content:space-between;font-size:7.5px;margin-top:-1px}
  .remember{display:flex;align-items:center;gap:5px}
  .toggle{width:24px;height:11px;border-radius:6px;background:#e9e9e9;position:relative}
  .toggle::after{content:"";position:absolute;left:1px;top:1px;width:9px;height:9px;border-radius:50%;background:#cfcfcf}
  .forgot{color:var(--ink-muted)}
  .login-form .btn{margin-top:10px}
  .signup{text-align:center;font-size:7.5px;color:var(--ink-muted);margin-top:24px}
  .signup a{color:var(--brand-red);font-weight:600;text-decoration:underline}

  .app-bar{position:absolute;left:0;right:0;top:0;background:var(--brand-red)}
  .app-bar .menu{position:absolute;left:16px;top:43px}
  .app-bar .wordmark{position:absolute;left:50%;top:42px;transform:translateX(-50%);font-size:9px}
  .app-bar .bag{position:absolute;right:14px;top:36px;width:27px;height:26px;border:1px solid rgba(255,255,255,.85);border-radius:5px;display:flex;align-items:center;justify-content:center}

  .screen--recipient .app-bar{height:112px}
  .promo{position:absolute;left:15px;right:14px;top:77px;height:77px;background:var(--white);border-radius:8px;box-shadow:0 2px 8px rgba(0,0,0,.12);padding:0 0 0 9px;display:flex;align-items:center}
  .promo h2{font-family:"Rubik",sans-serif;font-weight:600;font-size:10.5px;line-height:13px;width:100px}
  .art--celebrate{right:10px;top:8px;width:62px;height:60px;border-radius:6px;background:linear-gradient(160deg,#f6c54c 0%,#e85d4a 50%,#4a7fd1 100%)}
  .steps{position:absolute;left:11px;right:8px;top:173px;display:flex;align-items:center;gap:4px;font-size:7px;color:var(--ink-muted);white-space:nowrap}
  .step{display:flex;align-items:center;gap:4px}
  .step .num{width:15px;height:15px;border-radius:50%;border:1px solid var(--line);display:flex;align-items:center;justify-content:center;font-size:7px;color:var(--ink)}
  .step--active{color:var(--ink);font-weight:600}
  .step--active .num{background:var(--brand-red);border-color:var(--brand-red);color:var(--white)}
  .chev{color:#b5b5b5;font-size:8px}
  .recipient-body{position:absolute;left:15px;right:14px;top:202px}
  .recipient-body .title{font-size:15px}
  .recipient-body .lead{margin-top:6px}
  .recipient-form{margin-top:14px}
  .recipient-form .field{margin-bottom:12px}
  .recipient-form .btn{margin-top:2px}

  .screen--tutorial .app-bar{height:81px}
  .how{position:absolute;left:0;right:0;top:94px;text-align:center}
  .how .eyebrow{font-size:7px;color:var(--ink-muted)}
  .how .title{font-size:15px;margin-top:1px}
  .art--profiles{left:20px;top:142px;width:184px;height:184px;border-radius:8px;background:linear-gradient(160deg,#f3f3f3 0%,#e8e8e8 60%,#f1dcdb 100%)}
  .tutorial-lead{position:absolute;left:14px;right:14px;top:347px}
  .dots{position:absolute;left:0;right:0;top:396px;display:flex;justify-content:center;align-items:center;gap:8px}
  .dots span{width:7px;height:7px;border-radius:50%;background:var(--dot)}
  .dots .on{width:18px;border-radius:4px;background:var(--brand-red)}
  .screen--tutorial .btn{position:absolute;left:14px;right:13px;top:428px}

  .blob{position:absolute;border-radius:50%;background:var(--brand-red-soft);opacity:.45}
</style>
</head>
<body>

<section class="screen screen--splash">
  <div class="notch"></div>
  <div class="status">
    <span>9:41</span>
    <svg width="30" height="8" viewBox="0 0 30 8" fill="#fff"><rect x="0" y="5" width="2" height="3"/><rect x="3" y="3.5" width="2" height="4.5"/><rect x="6" y="2" width="2" height="6"/><path d="M11 3.5a5 5 0 0 1 7 0l-1 1a3.6 3.6 0 0 0-5 0z"/><circle cx="14.5" cy="6.6" r="1"/><rect x="21" y="1.5" width="9" height="5" rx="1.2"/></svg>
  </div>
  <div class="splash-mark">
    <div class="box"></div>
    <span class="wordmark">KELVA GIFTS</span>
  </div>
  <div class="art art--party" role="img" aria-label="Illustration of people celebrating among gift boxes and balloons"></div>
</section>

<section class="screen screen--login">
  <div class="login-hero">
    <div class="blob" style="width:140px;height:70px;left:90px;top:-20px"></div>
    <div class="art art--card" role="img" aria-label="Illustration of a man holding up a festive greeting card beside a potted plant"></div>
  </div>
  <div class="notch"></div>
  <div class="status">
    <span>9:41</span>
    <svg width="30" height="8" viewBox="0 0 30 8" fill="#fff"><rect x="0" y="5" width="2" height="3"/><rect x="3" y="3.5" width="2" height="4.5"/><rect x="6" y="2" width="2" height="6"/><path d="M11 3.5a5 5 0 0 1 7 0l-1 1a3.6 3.6 0 0 0-5 0z"/><circle cx="14.5" cy="6.6" r="1"/><rect x="21" y="1.5" width="9" height="5" rx="1.2"/></svg>
  </div>
  <div class="login-sheet">
    <h1 class="title">Welcome Back!</h1>
    <p class="lead">Login now to access back your Kelva account and<br>the whole features!</p>
    <div class="login-form">
      <div class="field">
        <label class="field-label">Email Address<span class="req">*</span></label>
        <div class="input"></div>
      </div>
      <div class="field">
        <label class="field-label">Password<span class="req">*</span></label>
        <div class="input">
          <svg width="11" height="8" viewBox="0 0 11 8" fill="none" stroke="#666" stroke-width="1"><path d="M.5 4S2.5.5 5.5.5 10.5 4 10.5 4 8.5 7.5 5.5 7.5.5 4 .5 4z"/><circle cx="5.5" cy="4" r="1.6"/></svg>
        </div>
      </div>
      <div class="remember-row">
        <span class="remember"><span class="toggle"></span>Remember me</span>
        <span class="forgot">Forgot password?</span>
      </div>
      <div class="btn">Login</div>
    </div>
    <p class="signup">Didn't have an account? <a>Sign Up</a></p>
  </div>
</section>

<section class="screen screen--recipient">
  <div class="app-bar">
    <div class="blob" style="width:130px;height:80px;left:40px;top:40px"></div>
    <div class="blob" style="width:90px;height:60px;left:150px;top:-20px"></div>
    <svg class="menu" width="14" height="10" viewBox="0 0 14 10" stroke="#fff" stroke-width="1.2"><path d="M0 1h14M0 5h14M0 9h14"/></svg>
    <span class="wordmark">KELVA GIFTS</span>
    <span class="bag"><svg width="11" height="10" viewBox="0 0 11 10" fill="none" stroke="#fff" stroke-width="1"><path d="M1 3.5h9v6H1z"/><path d="M3.5 3.5V2.5a2 2 0 0 1 4 0v1"/></svg></span>
  </div>
  <div class="notch"></div>
  <div class="status">
    <span>9:41</span>
    <svg width="30" height="8" viewBox="0 0 30 8" fill="#fff"><rect x="0" y="5" width="2" height="3"/><rect x="3" y="3.5" width="2" height="4.5"/><rect x="6" y="2" width="2" height="6"/><path d="M11 3.5a5 5 0 0 1 7 0l-1 1a3.6 3.6 0 0 0-5 0z"/><circle cx="14.5" cy="6.6" r="1"/><rect x="21" y="1.5" width="9" height="5" rx="1.2"/></svg>
  </div>
  <div class="promo">
    <h2>Feeling grateful for someone?</h2>
    <div class="art art--celebrate" role="img" aria-label="Illustration of friends jumping in celebration with confetti"></div>
  </div>
  <div class="steps">
    <span class="step step--active"><span class="num">1</span>Recipient</span><span class="chev">›</span>
    <span class="step"><span class="num">2</span>Greeting Card</span><span class="chev">›</span>
    <span class="step"><span class="num">3</span>Gift Cards</span>
  </div>
  <div class="recipient-body">
    <h1 class="title">Recipient</h1>
    <p class="lead">Enter your recipient information to send your<br>perfect digital gift</p>
    <div class="recipient-form">
      <div class="field">
        <label class="field-label">Name of Recipient<span class="req">*</span></label>
        <div class="input"></div>
      </div>
      <div class="field">
        <label class="field-label">Email of Recipient <span class="opt">(optional)</span></label>
        <div class="input"></div>
      </div>
      <div class="field">
        <label class="field-label">Country</label>
        <div class="input"><svg width="8" height="5" viewBox="0 0 8 5" fill="none" stroke="#666" stroke-width="1"><path d="M.5.5l3.5 3.5L7.5.5"/></svg></div>
      </div>
      <div class="btn">Next</div>
    </div>
  </div>
</section>

<section class="screen screen--tutorial">
  <div class="app-bar">
    <div class="blob" style="width:120px;height:60px;left:50px;top:-10px"></div>
    <svg class="menu" width="14" height="10" viewBox="0 0 14 10" stroke="#fff" stroke-width="1.2"><path d="M0 1h14M0 5h14M0 9h14"/></svg>
    <span class="wordmark">KELVA GIFTS</span>
    <span class="bag"><svg width="11" height="10" viewBox="0 0 11 10" fill="none" stroke="#fff" stroke-width="1"><path d="M1 3.5h9v6H1z"/><path d="M3.5 3.5V2.5a2 2 0 0 1 4 0v1"/></svg></span>
  </div>
  <div class="notch"></div>
  <div class="status">
    <span>9:41</span>
    <svg width="30" height="8" viewBox="0 0 30 8" fill="#fff"><rect x="0" y="5" width="2" height="3"/><rect x="3" y="3.5" width="2" height="4.5"/><rect x="6" y="2" width="2" height="6"/><path d="M11 3.5a5 5 0 0 1 7 0l-1 1a3.6 3.6 0 0 0-5 0z"/><circle cx="14.5" cy="6.6" r="1"/><rect x="21" y="1.5" width="9" height="5" rx="1.2"/></svg>
  </div>
  <div class="how">
    <p class="eyebrow">How it works</p>
    <h1 class="title">Recipient</h1>
  </div>
  <div class="art art--profiles" role="img" aria-label="Illustration of a man choosing among recipient profile cards"></div>
  <p class="lead tutorial-lead">Enter your recipient information to send your<br>perfect digital gift</p>
  <div class="dots"><span class="on"></span><span></span><span></span><span></span></div>
  <div class="btn">Continue</div>
</section>

</body>
</html>
```